Business Card Design for a Jockey's Agent

A business card design that helps to develop a brand or identity for myself, the agent, perhaps on one side with a clean minimalist design, and on the other side a simple design with the two jockeys names i currently represent. Those jockeys may change twice a year as they move around the country, switch agents, etc, so i think keeping one side designed to promote the agent and a second side that can be changed easily to identify the jockeys i currently represent would be the best.

Target Market(s)

Thoroughbred racehorse trainers

Industry/Entity Type

Business

Contact Information for Business Card

Garrett Lindqvist - Jockey Agent
mobile (614) 382 7291
garrettplindqvist7mailhub.example

Jockeys: Everett Kline, Tobias Renwick

Font styles to use
Serif

Requirements
Must have
• contact info and modern feel and font
Nice to have
• clean minimalist element of racing, jockey silk, helmut or crop, finish marker pole from racetrack etc,
Should not have
• DONT HAVE ANY KIND OF LOGO ETC. IMAGE IS ONE OF MY RACEHORSES TO HELP FINISH BRIEF.
• racing horse, stuffy vintage racing feel or Weekly Paddock Sheet fonts

```html
<!DOCTYPE html>
<html lang="en">
<head>
<meta charset="utf-8">
<title>Garrett Lindqvist — Jockey Agent Business Card</title>
<link rel="stylesheet" href="https://fonts.googleapis.com/css2?family=Raleway:wght@300;400&display=swap">
<style>
  :root {
    --backdrop: #d6d6d6;
    --card-dark: #050505;
    --card-light: #f1f1f0;
    --ink-light: #e8e8e8;
    --ink-dark: #1a1a1a;
    --art-dark-a: #2a2a2a;
    --art-dark-b: #111111;
    --art-light-a: #dcdcdc;
    --art-light-b: #ececec;
  }
  * { margin: 0; padding: 0; box-sizing: border-box; }
  html, body {
    width: 1200px;
    height: 900px;
    overflow: hidden;
    background: var(--backdrop);
    font-family: "Raleway", sans-serif;
  }
  .stage {
    position: relative;
    width: 1200px;
    height: 900px;
  }
  .card {
    position: absolute;
    width: 520px;
    height: 297px;
    overflow: hidden;
    text-transform: uppercase;
    font-weight: 300;
    letter-spacing: 0.02em;
  }
  .card--agent {
    left: 70px;
    top: 140px;
    background: var(--card-dark);
    color: var(--ink-light);
  }
  .card--roster {
    left: 590px;
    top: 437px;
    background: var(--card-light);
    color: var(--ink-dark);
  }
  .card__art {
    position: absolute;
    left: 110px;
    top: 40px;
    width: 330px;
    height: 257px;
    border-radius: 46% 46% 8% 8%;
  }
  .card--agent .card__art {
    background: radial-gradient(ellipse at 60% 55%, var(--art-dark-a), var(--art-dark-b) 72%, transparent 100%);
  }
  .card--roster .card__art {
    background: radial-gradient(ellipse at 60% 55%, var(--art-light-a), var(--art-light-b) 72%, transparent 100%);
  }
  .card__content {
    position: relative;
    text-align: center;
    width: 100%;
  }
  .agent-name {
    display: inline-block;
    margin-top: 88px;
    font-size: 25px;
    font-weight: 300;
    letter-spacing: 0.04em;
    border-top: 1.5px solid var(--ink-light);
    border-bottom: 1.5px solid var(--ink-light);
    padding: 1px 2px 0;
    line-height: 1.1;
  }
  .agent-title {
    margin-top: 4px;
    font-size: 15px;
    letter-spacing: 0.06em;
  }
  .agent-contact {
    margin-top: 14px;
    font-size: 11.5px;
    line-height: 1.5;
    letter-spacing: 0.05em;
    color: #cfcfcf;
  }
  .roster {
    padding-top: 82px;
  }
  .jockey + .jockey { margin-top: 14px; }
  .jockey__name {
    font-size: 27px;
    font-weight: 300;
    line-height: 1.05;
    letter-spacing: 0.02em;
  }
  .jockey__weight {
    font-size: 12px;
    letter-spacing: 0.04em;
  }
</style>
</head>
<body>
  <main class="stage">
    <section class="card card--agent" aria-label="Agent side of business card">
      <div class="card__art" role="img" aria-label="Faint line illustration of racehorses with jockeys"></div>
      <div class="card__content">
        <h1 class="agent-name">Garrett Lindqvist</h1>
        <p class="agent-title">Jockey Agent</p>
        <p class="agent-contact">
          Mobile: (614) 382 7291<br>
          Email: garrettplindqvist7mailhub.example
        </p>
      </div>
    </section>

    <section class="card card--roster" aria-label="Jockey roster side of business card">
      <div class="card__art" role="img" aria-label="Faint line illustration of racehorses with jockeys"></div>
      <div class="card__content roster">
        <div class="jockey">
          <p class="jockey__name">Everett Kline</p>
          <p class="jockey__weight">112lbs</p>
        </div>
        <div class="jockey">
          <p class="jockey__name">Tobias Renwick</p>
          <p class="jockey__weight">114lbs</p>
        </div>
      </div>
    </section>
  </main>
</body>
</html>
```